OM sidrawi Multibrand Web Design

We need Simple but very Elegant Website for Our EL hafeez Company based in Kuwait, We are not good in describing design but we need simple but elegant and responsive to attract new market and to enable us competing in business

It Company

```html
<!DOCTYPE html>
<html lang="en">
<head>
<meta charset="utf-8">
<title>EL hafeez — Website</title>
<link rel="stylesheet" href="https://fonts.googleapis.com/css2?family=Oswald:wght@300;400;500&family=Open+Sans:wght@400;600;700&family=Montserrat:wght@600&display=swap">
<style>
:root{
  --bg:#0e58a6;
  --dark:#272727;
  --red:#f2464b;
  --slate:#4b5563;
  --grey:#e5e9ec;
  --text:#7d8590;
  --navy:#2d3b48;
  --white:#ffffff;
}
*{box-sizing:border-box;margin:0;padding:0}
html,body{width:1200px;height:1200px;overflow:hidden;background:var(--bg)}
.page{position:absolute;left:269px;top:0;width:690px;height:1250px;transform:scale(.96);transform-origin:0 0;background:var(--white);font-family:"Open Sans",sans-serif;color:var(--text);overflow:hidden}
.abs{position:absolute}
.head{font-family:"Oswald",sans-serif;font-weight:400;color:var(--slate)}
/* header */
.topbar{left:0;top:0;width:690px;height:48px;background:var(--dark)}
.brand{left:92px;top:14px;display:flex;align-items:center;gap:7px;font-family:"Oswald",sans-serif;font-weight:500;font-size:17px;color:var(--white);letter-spacing:.3px}
.brand-mark{width:12px;height:12px;background:var(--red)}
.nav{left:424px;top:19px;display:flex;gap:8px;font-family:"Oswald",sans-serif;font-size:8.5px;color:var(--white)}
.nav .active{color:var(--red)}
.nav-pointer{left:427px;top:41px;width:0;height:0;border-left:6px solid transparent;border-right:6px solid transparent;border-bottom:7px solid var(--white)}
/* hero */
.hero{left:0;top:48px;width:690px;height:259px;background:linear-gradient(180deg,#4a4c50 0%,#3a3c40 45%,#2c2c2e 100%)}
.avatar{left:309px;top:67px;width:72px;height:72px;border-radius:50%;background:linear-gradient(160deg,#8a8f96,#3a3d42);border:2px solid #6a6d72}
.hero-title{left:0;top:149px;width:690px;text-align:center;font-family:"Montserrat",sans-serif;font-weight:600;font-size:14.5px;line-height:15.5px;color:var(--white);letter-spacing:.4px}
.hero-copy{left:195px;top:190px;width:300px;text-align:center;font-size:5.6px;line-height:9.5px;color:#d8d8d8}
.btn{font-family:"Open Sans",sans-serif;font-weight:600;font-size:7px;text-align:center;line-height:22px;height:22px}
.btn-red{left:281px;top:230px;width:62px;background:var(--red);color:var(--white)}
.btn-white{left:346px;top:230px;width:62px;background:var(--white);color:var(--dark)}
.arrow{width:20px;height:20px;border-radius:50%}
.arrow-l{left:93px;top:174px;background:#1c1c1c}
.arrow-r{left:576px;top:174px;background:var(--red)}
/* services */
.service{width:120px;text-align:center;top:335px}
.service .pic{width:86px;height:86px;border-radius:50%;margin:0 auto}
.service h3{font-family:"Oswald",sans-serif;font-weight:400;font-size:14px;color:var(--slate);margin-top:12px}
.service p{font-size:4.8px;line-height:7.8px;margin-top:5px;padding:0 6px}
.service .more{display:inline-block;margin-top:8px;width:31px;height:17px;line-height:17px;font-size:5.5px;font-weight:700;color:var(--white);background:var(--red)}
.service .more.muted{background:#5a6470}
/* latest works */
.works{left:0;top:532px;width:690px;height:228px;background:var(--grey)}
.works-title{left:92px;top:550px;font-size:13px}
.dots{left:544px;top:556px;display:flex;gap:2px}
.dots span{width:7px;height:7px;border-radius:50%;background:#5a6470}
.dots span.on{background:var(--red)}
.work{top:575px;width:246px;height:169px}
.work-caption{left:227px;top:822px}
/* offers */
.col-title{font-size:16px;top:790px}
.thumb{width:88px;height:96px;top:818px}
.thumb-nav{width:16px;height:16px;border-radius:50%;background:var(--red);top:824px}
.col-text{width:104px;top:922px;font-size:4.8px;line-height:8.6px}
.col-text b{display:block;color:var(--dark);font-size:5px}
.divider-v{left:351px;top:778px;width:1px;height:208px;background:#dfe2e5}
.offer-title{left:394px;top:786px;font-family:"Oswald",sans-serif;font-weight:400;font-size:20px;line-height:21px;color:var(--red)}
.offer-list{left:394px;top:849px;width:203px}
.offer-item{height:32px;border-bottom:1px solid #e1e4e7;display:flex;align-items:center;gap:7px;font-family:"Oswald",sans-serif;font-size:8px;color:var(--slate)}
.offer-item .dot{width:13px;height:13px;border-radius:50%;background:var(--red);display:flex;align-items:center;justify-content:center}
.offer-tab{height:25px;width:185px;background:var(--red);color:var(--white);font-family:"Oswald",sans-serif;font-size:8px;padding-left:20px;line-height:25px;clip-path:polygon(0 0,93% 0,100% 50%,93% 100%,0 100%)}
/* clients */
.clients-title{left:92px;top:998px;font-size:10px}
.clients-rule{left:146px;top:1009px;width:451px;height:1px;background:#d5d9dd}
.clients{left:92px;top:1024px;width:505px;display:flex;justify-content:space-between;align-items:center;font-family:"Montserrat",sans-serif;font-weight:600;color:#9aa3ad}
.to-top{left:624px;top:1060px;width:18px;height:18px;border-radius:50%;background:#d9dde1}
.notice{left:92px;top:1078px;width:505px;height:27px;background:var(--red);color:var(--white);font-size:4.8px;line-height:7.5px;text-align:center;padding-top:6px}
/* footer */
.footer{left:0;top:1105px;width:690px;height:121px;background:var(--grey)}
.foot-brand{left:93px;top:1122px;font-family:"Oswald",sans-serif;font-weight:500;font-size:15px;color:var(--red)}
.socials{left:93px;top:1148px;display:flex;gap:5px}
.socials span{width:15px;height:15px;border-radius:50%;background:var(--white);border:1px solid #d2d6da}
.foot-col{top:1122px;width:110px}
.foot-col h4{font-family:"Oswald",sans-serif;font-weight:400;font-size:8.5px;color:var(--slate);margin-bottom:6px}
.foot-col p{font-size:4.6px;line-height:10.3px;color:#99a1aa;text-transform:uppercase}
.email{left:480px;top:1140px;width:117px;height:13px;background:#d7dbdf;font-size:4.8px;line-height:13px;padding-left:6px;color:#6d7580}
.submit{left:545px;top:1160px;width:52px;height:15px;background:var(--red);color:var(--white);font-size:6px;text-align:center;line-height:15px}
.bottom{left:0;top:1226px;width:690px;height:24px;background:var(--navy);color:#c5ccd3;font-family:"Oswald",sans-serif;font-size:6px;text-align:center;line-height:26px}
</style>
</head>
<body>
<main class="page">
  <!-- header -->
  <div class="abs topbar"></div>
  <div class="abs brand"><span class="brand-mark"></span>EL hafeez</div>
  <nav class="abs nav"><span class="active">HOME</span><span>ABOUT</span><span>PROJECTS</span><span>BLOG</span><span>CONTACTS</span></nav>
  <div class="abs nav-pointer"></div>

  <!-- hero -->
  <section class="abs hero" role="img" aria-label="City skyline of tall towers under a cloudy sky"></section>
  <div class="abs avatar" role="img" aria-label="Portrait of a business woman"></div>
  <h1 class="abs hero-title">CONSTANT DEVELOPMENT OF<br>NEW TECHNOLOGIES</h1>
  <p class="abs hero-copy">Lorem ipsum dolor sit amet, consectetur adipiscing elit, sed do eiusmod tempor incididunt ut labore et dolore magna aliqua. Ut enim ad minim veniam, quis nostrud exercitation ullamco laboris nisi aliquip</p>
  <div class="abs btn btn-red">CLICK HERE</div>
  <div class="abs btn btn-white">JOIN US</div>
  <svg class="abs arrow arrow-l" viewBox="0 0 20 20"><path d="M11.5 6.5 8 10l3.5 3.5" fill="none" stroke="#fff" stroke-width="1.8"/></svg>
  <svg class="abs arrow arrow-r" viewBox="0 0 20 20"><path d="M8.5 6.5 12 10l-3.5 3.5" fill="none" stroke="#fff" stroke-width="1.8"/></svg>

  <!-- services -->
  <div class="abs service" style="left:91px">
    <div class="pic" role="img" aria-label="Surveyor with yellow helmet at a site" style="background:linear-gradient(150deg,#c9ced3,#8b939b)"></div>
    <h3>PLANNING</h3>
    <p>Aliquam elit, sed do eiusmod tempor incidunt ut labore et dolore magna. Aliqua enim ad minim veniam, quis nostrud exercitation des.</p>
    <span class="more muted">MORE</span>
  </div>
  <div class="abs service" style="left:220px">
    <div class="pic" role="img" aria-label="Architectural drawings on a desk" style="background:linear-gradient(150deg,#e9ecef,#b9c0c7 60%,#e59a5a)"></div>
    <h3>ANALYSIS</h3>
    <p>Aliquam elit, sed do eiusmod tempor incidunt ut labore et dolore magna. Aliqua enim ad minim veniam, quis nostrud exercitation des.</p>
    <span class="more">MORE</span>
  </div>
  <div class="abs service" style="left:349px">
    <div class="pic" role="img" aria-label="Modern building with a pool at sunset" style="background:linear-gradient(170deg,#7b8896,#d6b68d 55%,#3e8fb0)"></div>
    <h3>MODELING</h3>
    <p>Aliquam elit, sed do eiusmod tempor incidunt ut labore et dolore magna. Aliqua enim ad minim veniam, quis nostrud exercitation des.</p>
    <span class="more">MORE</span>
  </div>
  <div class="abs service" style="left:479px">
    <div class="pic" role="img" aria-label="Warm lit interior with wooden ceiling" style="background:linear-gradient(160deg,#f0c48a,#c98a4a 55%,#eee)"></div>
    <h3>DESIGN</h3>
    <p>Aliquam elit, sed do eiusmod tempor incidunt ut labore et dolore magna. Aliqua enim ad minim veniam, quis nostrud exercitation des.</p>
    <span class="more">MORE</span>
  </div>

  <!-- latest works -->
  <section class="abs works"></section>
  <h2 class="abs head works-title">LATEST WORKS</h2>
  <div class="abs dots"><span></span><span></span><span></span><span class="on"></span><span></span><span></span></div>
  <div class="abs work" style="left:92px;background:linear-gradient(180deg,#3f7fc4 0%,#a9c9e6 45%,#e8e8e6 46%,#b3473a 70%,#3b3b3b)" role="img" aria-label="White modern house with red brick wall"></div>
  <div class="abs work" style="left:351px;background:linear-gradient(180deg,#6fa6d8 0%,#c7dcee 35%,#e9ecee 50%,#7e8a8e 75%,#5c9c6a)" role="img" aria-label="Glass pavilion house with a pool"></div>
  <div class="abs" style="left:227px;top:823px;width:111px;height:21px;background:rgba(40,40,40,.75)"></div>
  <svg class="abs" style="left:321px;top:827px" width="13" height="13" viewBox="0 0 13 13"><circle cx="6.5" cy="6.5" r="6.5" fill="#1c1c1c"/><circle cx="6" cy="6" r="2.2" fill="none" stroke="#fff" stroke-width=".9"/><path d="M7.6 7.6 9.4 9.4" stroke="#fff" stroke-width=".9"/></svg>

  <!-- commercial / budget -->
  <h2 class="abs head col-title" style="left:92px">Commercial</h2>
  <div class="abs thumb" style="left:92px;background:linear-gradient(170deg,#3b7fc8,#b6d2ec 55%,#3d3d3d)" role="img" aria-label="Glass office facade"></div>
  <svg class="abs thumb-nav" style="left:169px" viewBox="0 0 16 16"><path d="M9 5 6 8l3 3" fill="none" stroke="#fff" stroke-width="1.5"/></svg>
  <p class="abs col-text" style="left:92px"><b>LOREM IPSUM DOLOR SIT</b>Amet, consectetur adipiscing elit, sed diam nonummy nibh euismod tincidunt laoreet dolore magna aliquam massa laoreet. Erat volutpat enim ad minim venia.</p>

  <h2 class="abs head col-title" style="left:222px">Budget</h2>
  <div class="abs thumb" style="left:222px;background:linear-gradient(175deg,#a9b4bc,#e2d5bd 50%,#4a5a3a)" role="img" aria-label="Lit villa with palm trees at dusk"></div>
  <svg class="abs thumb-nav" style="left:300px" viewBox="0 0 16 16"><path d="M7 5l3 3-3 3" fill="none" stroke="#fff" stroke-width="1.5"/></svg>
  <p class="abs col-text" style="left:222px"><b>LOREM IPSUM DOLOR SIT</b>Amet, consectetur adipiscing elit, sed diam nonummy nibh euismod tincidunt laoreet dolore magna aliquam massa laoreet. Erat volutpat enim ad minim venia.</p>

  <div class="abs divider-v"></div>

  <h2 class="abs offer-title">What We<br>Offer</h2>
  <div class="abs offer-list">
    <div class="offer-tab">GREEN TECHNOLOGY</div>
    <div class="offer-item"><span class="dot"><svg width="7" height="7" viewBox="0 0 7 7"><path d="M2.5 1.2 4.8 3.5 2.5 5.8" fill="none" stroke="#fff" stroke-width="1.2"/></svg></span>HIGH STANDARDS</div>
    <div class="offer-item"><span class="dot"><svg width="7" height="7" viewBox="0 0 7 7"><path d="M2.5 1.2 4.8 3.5 2.5 5.8" fill="none" stroke="#fff" stroke-width="1.2"/></svg></span>QUALITY CONTROL</div>
    <div class="offer-item" style="border-bottom:none"><span class="dot"><svg width="7" height="7" viewBox="0 0 7 7"><path d="M2.5 1.2 4.8 3.5 2.5 5.8" fill="none" stroke="#fff" stroke-width="1.2"/></svg></span>UNIQUE SOLUTIONS</div>
  </div>

  <!-- clients -->
  <h2 class="abs head clients-title">Our Clients</h2>
  <div class="abs clients-rule"></div>
  <div class="abs clients">
    <span style="font-size:15px">NORVA</span>
    <span style="font-size:15px">BRIXO</span>
    <span style="font-size:21px">KL88</span>
    <span style="font-size:11px">DUNEWAY</span>
    <span style="font-size:12px">TALLIS</span>
    <span style="font-size:11px">ARDENT</span>
  </div>
  <svg class="abs to-top" viewBox="0 0 18 18"><path d="M5.5 10.5 9 7l3.5 3.5" fill="none" stroke="#2a2a2a" stroke-width="1.6"/></svg>
  <div class="abs notice">Lorem ipsum dolor sit amet, consectetur adipiscing elit. Sed cumque distinctio labore minima ipsum fugit aspernatur dolore deserunt iure sunt.<br>Lorem ipsum dolor sit amet, consectetur adipiscing elit, sed do eiusmod tempor incididunt ut labore.</div>

  <!-- footer -->
  <footer class="abs footer"></footer>
  <div class="abs foot-brand">EL hafeez</div>
  <div class="abs socials"><span></span><span></span><span></span><span></span><span></span></div>
  <div class="abs foot-col" style="left:222px">
    <h4>OUR LOCATION</h4>
    <p>12 Harbour Lane,<br>Salmiya, KW 20 AB<br><br>Freephone: +1 800 000 1200<br>Telephone: +1 800 000 3400<br>Fax: +1 800 000 5600</p>
  </div>
  <div class="abs foot-col" style="left:351px">
    <h4>OVERVIEW</h4>
    <p>What we do<br>Sales for services<br>Development process<br>Clients<br>Our team<br>Blog</p>
  </div>
  <div class="abs foot-col" style="left:480px">
    <h4>NEWSLETTER</h4>
  </div>
  <div class="abs email">ENTER YOUR EMAIL</div>
  <div class="abs submit">SUBMIT</div>
  <div class="abs bottom">© 2006–2018. ALL RIGHTS RESERVED.</div>
</main>
</body>
</html>
```